Vordaline - Fitness Coach. Needs a Business Card Design that I can also use for other advertising

Established 2012, I have finished the KTRB National Certificate in Fitness & Personal Training. Harlow Cross First Aid Certificate. I have the Auckland 800m track records for MW45. I also came 1st at the 2012 Pellamar Games in 800 & 1500m. I am passionate about health & fitness and would like to help people reach their health & fitness goals. I also take health & fitness weekends. Main interests - Running, Weight Training, Yoga & Aqua Jogging. I like strength/power, but am femine.

Target Market(s)

Male or Female 18 and over that wants to improve their health & fitness

Industry/Entity Type

Advertising

Requirements
Must have
• my name: Rosalind K Tarbury contact details: ros@quillsend.co.nz mobile - 021 583917 URL name: facebook.com/rosalindKtarbury - VordaLine
Photo of Me

```html
<!DOCTYPE html>
<html lang="en">
<head>
<meta charset="utf-8">
<title>Rosalind K Tarbury – Vordaline Fitness Coach</title>
<link href="https://fonts.googleapis.com/css2?family=Carlito&display=swap" rel="stylesheet">
<style>
  :root {
    --paper: #ffffff;
    --lime: #66ff00;
    --name-green: #3fcc12;
    --text-light: #ffffff;
    --foliage-dark: #1f3a12;
    --foliage-mid: #3d6b22;
    --grass: #7cc04a;
  }
  html, body {
    margin: 0;
    padding: 0;
    overflow: hidden;
    background: var(--paper);
  }
  .card {
    position: relative;
    width: 1200px;
    height: 855px;
    background: var(--paper);
    font-family: "Carlito", "Calibri", sans-serif;
    overflow: hidden;
  }
  .card__wave {
    position: absolute;
    inset: 0;
    width: 1200px;
    height: 855px;
  }
  .card__wave path { fill: var(--lime); }
  .portrait {
    position: absolute;
    left: 7px;
    top: 28px;
    width: 194px;
    height: 261px;
    background: linear-gradient(180deg, var(--foliage-dark) 0%, var(--foliage-mid) 70%, var(--grass) 100%);
  }
  .contact {
    position: absolute;
    left: 633px;
    top: 318px;
    margin: 0;
    padding: 0;
    list-style: none;
    color: var(--text-light);
    font-size: 50px;
    line-height: 71px;
  }
  .coach-name {
    position: absolute;
    left: 10px;
    top: 764px;
    margin: 0;
    color: var(--name-green);
    font-size: 45px;
    font-weight: 400;
    line-height: 60px;
  }
</style>
</head>
<body>
  <div class="card">
    <svg class="card__wave" viewBox="0 0 1200 855" aria-hidden="true">
      <path d="M499 0 Q664 427 502 855 L1200 855 L1200 0 Z"/>
    </svg>
    <div class="portrait" role="img" aria-label="Photo of the coach leaping in the air in front of green foliage"></div>
    <ul class="contact">
      <li>ros@quillsend.co.nz</li>
      <li>Call me - 021 583917</li>
      <li>facebook - Vordaline</li>
    </ul>
    <h1 class="coach-name">Rosalind K Tarbury</h1>
  </div>
</body>
</html>
```